Kowhai Crest (Podiatry and Physiotherapy) Clinical Brochure

You are producing a brochure that will sit in clinical/medical waiting rooms for our business Kowhai Crest. A clinic that providers podiatry and physiotherapy services.

As you can see on our website www.kowhaicrest.example.nz we provide 6 different brands/services:
- Clearbloom Care
- Brightedge Relief Studio
- Stepsure Works
- Riverstone Motion Renewal
- Pearlgleam Studio
- Tidewater Everyday Care

People will generally have found us through an ad e.g. search fungal nail treatment and end up straight on www.clearbloomcare.example.nz and therefore, each of the brands should be seen as being separate entities although part of the bigger brand Kowhai Crest.

We are looking at a brochure (open to bi-fold, tri-fold etc.) that highlights all of our brands as well as the services that each of our brands provide which can be found on each of the websites listed above. We want this to be professional and informative yet simple and easy to read - this interpretation can be somewhat left up to you. This brochure will sit in waiting rooms/clinical environments.

I have attached our brand strategy so that you can understand our fonts and colours. I have also attached our logos for reference.

```html
<!DOCTYPE html>
<html lang="en">
<head>
<meta charset="utf-8">
<title>Kowhai Crest Brochure – Inside Spread</title>
<link rel="stylesheet" href="https://fonts.googleapis.com/css2?family=Montserrat:wght@500;600;700&family=Arimo:wght@700&family=Saira+Extra+Condensed:wght@200&family=Tenor+Sans&family=Open+Sans:wght@400&display=swap">
<style>
  :root {
    --mat: #c3e2fe;
    --navy: #0c3a86;
    --mid-blue: #3372b9;
    --tag-blue: #3574bc;
    --sky: #5ea3e8;
    --mist: #e8e9ee;
    --white: #ffffff;
    --brand-blue: #3571bd;
    --accent-red: #e03c31;
    --ink: #111111;
  }
  * { margin: 0; padding: 0; box-sizing: border-box; }
  html, body {
    width: 1200px; height: 1000px; overflow: hidden;
    background: var(--mat);
  }
  .canvas { position: relative; width: 1200px; height: 1000px; }

  .spread {
    position: absolute; left: 53px; top: 101px;
    width: 1094px; height: 773px;
    display: flex;
  }
  .panel { position: relative; width: 365px; height: 100%; overflow: hidden; }
  .panel--about {
    width: 364px;
    background: linear-gradient(90deg, var(--navy) 0%, var(--mid-blue) 100%);
    color: var(--white);
  }
  .panel--services {
    background: linear-gradient(90deg, var(--mist) 0%, var(--mid-blue) 100%);
  }

  .about-tag {
    position: absolute; left: 31px; top: 49px;
    width: 299px; height: 41px;
    background: var(--tag-blue);
    font-family: "Montserrat", sans-serif; font-weight: 700;
    font-size: 17px; letter-spacing: 3.4px;
    line-height: 41px; padding-left: 11px;
    white-space: nowrap;
  }
  .about-kicker {
    position: absolute; left: 31px; top: 118px;
    font-family: "Arimo", sans-serif; font-weight: 700;
    font-size: 24px; color: var(--sky);
    white-space: nowrap;
  }
  .about-type {
    position: absolute; left: 0; top: 0; width: 364px; height: 773px;
  }
  .about-title {
    font-family: "Arimo", sans-serif; font-weight: 700; font-size: 52px;
    fill: var(--white);
  }
  .about-body {
    font-family: "Saira Extra Condensed", "Arial Narrow", sans-serif;
    font-weight: 200; font-size: 40px; fill: var(--white);
  }
  .about-rule {
    position: absolute; left: 31px; top: 282px;
    width: 273px; height: 3px;
    background: linear-gradient(90deg, #e6e6ea 0%, rgba(230,230,234,0.2) 100%);
    clip-path: polygon(0 0, 100% 40%, 100% 60%, 0 100%);
  }

  .services-heading {
    position: absolute; left: 0; top: 0; width: 365px; height: 773px;
  }
  .services-heading-text {
    font-family: "Tenor Sans", sans-serif; font-size: 96px;
  }

  .service-card {
    position: absolute; height: 89px; background: var(--white);
    padding-top: 19px; white-space: nowrap;
  }
  .service-card--left {
    left: 91px; width: 274px;
    border-radius: 45px 0 0 45px;
    padding-left: 64px;
  }
  .service-card--right {
    left: 0; width: 305px;
    border-radius: 0 45px 45px 0;
    padding-left: 29px;
  }
  .service-brand {
    font-family: "Montserrat", sans-serif; font-weight: 700;
    font-size: 27px; color: var(--brand-blue); line-height: 1.1;
  }
  .service-name {
    font-family: "Montserrat", sans-serif; font-weight: 500;
    font-size: 14px; color: var(--accent-red); margin-top: 9px;
  }

  .spread-label {
    position: absolute; left: 0; width: 1200px; top: 905px;
    text-align: center;
    font-family: "Open Sans", sans-serif; font-size: 46px; color: var(--ink);
  }
</style>
</head>
<body>
<div class="canvas">
  <div class="spread">
    <section class="panel panel--about">
      <div class="about-tag">ABOUT KOWHAI CREST</div>
      <div class="about-kicker">WE ARE THE BEST IN</div>
      <div class="about-rule"></div>
      <svg class="about-type" viewBox="0 0 364 773">
        <text class="about-title" x="31" y="222" textLength="286" lengthAdjust="spacingAndGlyphs">FOOT HEALT</text>
        <g class="about-body">
          <text x="31" y="373" textLength="308" lengthAdjust="spacingAndGlyphs">With four state-of-the-art</text>
          <text x="31" y="430" textLength="308" lengthAdjust="spacingAndGlyphs">facilities in Auckland City,</text>
          <text x="31" y="487" textLength="308" lengthAdjust="spacingAndGlyphs">Hamilton, Tauranga and North</text>
          <text x="31" y="544" textLength="308" lengthAdjust="spacingAndGlyphs">Shore, you can be sure you're</text>
          <text x="31" y="601" textLength="308" lengthAdjust="spacingAndGlyphs">getting the best treatment for</text>
          <text x="31" y="658" textLength="308" lengthAdjust="spacingAndGlyphs">your foot condition, to put the</text>
          <text x="31" y="715" textLength="259" lengthAdjust="spacingAndGlyphs">bounce back in your step.</text>
        </g>
      </svg>
    </section>

    <section class="panel panel--services">
      <svg class="services-heading" viewBox="0 0 365 773" role="img" aria-label="Our Services">
        <defs>
          <linearGradient id="headingFade" gradientUnits="userSpaceOnUse" x1="0" y1="107" x2="0" y2="739">
            <stop offset="0" stop-color="#1d4f9a"/>
            <stop offset="0.45" stop-color="#7e9fc6"/>
            <stop offset="1" stop-color="#dfe3ea"/>
          </linearGradient>
        </defs>
        <text class="services-heading-text" transform="translate(80 739) rotate(-90)" x="0" y="0"
              textLength="632" lengthAdjust="spacingAndGlyphs"
              fill="url(#headingFade)">OUR SERVICES</text>
      </svg>
      <div class="service-card service-card--left" style="top:45px">
        <div class="service-brand">Kowhai Crest</div>
        <div class="service-name">Clearbloom Care</div>
      </div>
      <div class="service-card service-card--left" style="top:302px">
        <div class="service-brand">Kowhai Crest</div>
        <div class="service-name">Riverstone Motion Renewal</div>
      </div>
      <div class="service-card service-card--left" style="top:540px">
        <div class="service-brand">Kowhai Crest</div>
        <div class="service-name">Stepsure Works</div>
      </div>
    </section>

    <section class="panel panel--services">
      <div class="service-card service-card--right" style="top:166px">
        <div class="service-brand">Kowhai Crest</div>
        <div class="service-name">Brightedge Relief Studio</div>
      </div>
      <div class="service-card service-card--right" style="top:421px">
        <div class="service-brand">Kowhai Crest</div>
        <div class="service-name">Pearlgleam Studio</div>
      </div>
      <div class="service-card service-card--right" style="top:661px">
        <div class="service-brand">Kowhai Crest</div>
        <div class="service-name">Tidewater Everyday Care</div>
      </div>
    </section>
  </div>
  <div class="spread-label">inside</div>
</div>
</body>
</html>
```